Creative Design "Size Chart" for a Clothing Product

Hi, My dear friends! I am looking to do a contest to design a unique creative "Size Chart" for our clothing line. See Attached the Sizes & Ideas Thanks Good Luck Dorian

Colors

Designer to choose colors to be used in the design.

```html
<!DOCTYPE html>
<html lang="en">
<head>
<meta charset="utf-8">
<title>Size Chart</title>
<link href="https://fonts.googleapis.com/css2?family=PT+Sans:wght@400;700&display=swap" rel="stylesheet">
<style>
  :root {
    --page: #ffffff;
    --band: #7490ab;
    --label-bg: #eeeff1;
    --chest: #3a4f66;
    --waist: #2b9ad8;
    --divider: #a7d2ea;
    --row-line: #e3e8ee;
    --garment: #dde3ec;
  }
  html, body { margin: 0; padding: 0; }
  body {
    width: 1165px; height: 1200px; overflow: hidden;
    background: var(--page);
    font-family: "PT Sans", Arial, sans-serif;
    position: relative;
  }
  .header-band {
    position: absolute; left: 279px; top: 247px; width: 634px; height: 51px;
    background: var(--band);
  }
  .header-title {
    position: absolute; left: 279px; top: 258px; width: 634px; text-align: center;
    color: #fff; font-weight: 700; font-size: 25px; line-height: 30px; letter-spacing: 0.2px;
  }
  .garment {
    position: absolute; background: var(--garment); border-radius: 14px 14px 4px 4px;
  }
  .divider { position: absolute; height: 1px; background: var(--divider); }
  .size-table { position: absolute; height: 70px; }
  .size-table .head {
    position: absolute; left: 0; top: 0; right: 0; height: 17px; background: var(--band);
  }
  .size-table .label-col {
    position: absolute; left: 0; top: 17px; height: 52px; background: var(--label-bg);
  }
  .size-table .row-line {
    position: absolute; right: 0; top: 43px; height: 1px; background: var(--row-line);
  }
  .cell {
    position: absolute; transform: translateX(-50%); white-space: nowrap;
    font-size: 13.5px; line-height: 17px;
  }
  .cell.h { top: 0; color: #fff; }
  .cell.chest { top: 24px; color: var(--chest); }
  .cell.waist { top: 48px; color: var(--waist); }
  .womens .cell.h { font-size: 12.5px; }
</style>
</head>
<body>

<div class="header-band" role="img" aria-label="Tape measure band with ruler markings"></div>
<div class="header-title">SIZE CHART</div>

<div class="garment" role="img" aria-label="Men's polo shirt with chest and waist measurement lines" style="left:282px;top:341px;width:116px;height:144px"></div>
<div class="size-table mens" style="left:430px;top:374px;width:477px">
  <div class="head"></div><div class="label-col" style="width:69px"></div><div class="row-line" style="left:69px"></div>
  <span class="cell h" style="left:34px">Mens</span>
  <span class="cell h" style="left:103px">S</span><span class="cell h" style="left:168px">M</span><span class="cell h" style="left:237px">L</span><span class="cell h" style="left:307px">XL</span><span class="cell h" style="left:377px">2XL</span><span class="cell h" style="left:443px">3XL</span>
  <span class="cell chest" style="left:34px">Chest</span>
  <span class="cell chest" style="left:103px">34-36</span><span class="cell chest" style="left:168px">36-38</span><span class="cell chest" style="left:237px">38-40</span><span class="cell chest" style="left:307px">40-42</span><span class="cell chest" style="left:377px">43-45</span><span class="cell chest" style="left:443px">45-48</span>
  <span class="cell waist" style="left:34px">Waist</span>
  <span class="cell waist" style="left:103px">28-30</span><span class="cell waist" style="left:168px">30-32</span><span class="cell waist" style="left:237px">32-34</span><span class="cell waist" style="left:307px">34-36</span><span class="cell waist" style="left:377px">36-40</span><span class="cell waist" style="left:443px">40-44</span>
</div>
<div class="divider" style="left:297px;top:504px;width:608px"></div>

<div class="garment" role="img" aria-label="Women's fitted polo shirt with chest and waist measurement lines" style="left:289px;top:526px;width:111px;height:141px"></div>
<div class="size-table womens" style="left:430px;top:556px;width:481px">
  <div class="head"></div><div class="label-col" style="width:62px"></div><div class="row-line" style="left:62px"></div>
  <span class="cell h" style="left:30px">Womens</span>
  <span class="cell h" style="left:91px">XS (0-2)</span><span class="cell h" style="left:149px">S (4-6)</span><span class="cell h" style="left:210px">M (8-10)</span><span class="cell h" style="left:271px">L (12-14)</span><span class="cell h" style="left:334px">XL (14-16)</span><span class="cell h" style="left:391px">2XL (18)</span><span class="cell h" style="left:450px">3XL (20)</span>
  <span class="cell chest" style="left:30px">Chest</span>
  <span class="cell chest" style="left:91px">32-34</span><span class="cell chest" style="left:149px">34-36</span><span class="cell chest" style="left:210px">36-38</span><span class="cell chest" style="left:271px">38-40</span><span class="cell chest" style="left:334px">40-42</span><span class="cell chest" style="left:391px">42-44</span><span class="cell chest" style="left:450px">44-46</span>
  <span class="cell waist" style="left:30px">Waist</span>
  <span class="cell waist" style="left:91px">26-28</span><span class="cell waist" style="left:149px">28-30</span><span class="cell waist" style="left:210px">30-32</span><span class="cell waist" style="left:271px">32-34</span><span class="cell waist" style="left:334px">34-36</span><span class="cell waist" style="left:391px">36-38</span><span class="cell waist" style="left:450px">38-40</span>
</div>
<div class="divider" style="left:297px;top:689px;width:608px"></div>

<div class="garment" role="img" aria-label="Boys' crew neck t-shirt with chest and waist measurement lines" style="left:287px;top:718px;width:110px;height:101px"></div>
<div class="size-table boys" style="left:431px;top:733px;width:477px">
  <div class="head"></div><div class="label-col" style="width:69px"></div><div class="row-line" style="left:69px"></div>
  <span class="cell h" style="left:34px">Boys</span>
  <span class="cell h" style="left:103px">XXS</span><span class="cell h" style="left:168px">XS</span><span class="cell h" style="left:237px">S</span><span class="cell h" style="left:307px">M</span><span class="cell h" style="left:377px">L</span><span class="cell h" style="left:443px">XL</span>
  <span class="cell chest" style="left:34px">Chest</span>
  <span class="cell chest" style="left:103px">20-23</span><span class="cell chest" style="left:168px">23-26</span><span class="cell chest" style="left:237px">26-29</span><span class="cell chest" style="left:307px">29-32</span><span class="cell chest" style="left:377px">32-35</span><span class="cell chest" style="left:443px">35-38</span>
  <span class="cell waist" style="left:34px">Waist</span>
  <span class="cell waist" style="left:103px">19-21</span><span class="cell waist" style="left:168px">21-23</span><span class="cell waist" style="left:237px">22-25</span><span class="cell waist" style="left:307px">25-27</span><span class="cell waist" style="left:377px">27-29</span><span class="cell waist" style="left:443px">29-31</span>
</div>
<div class="divider" style="left:301px;top:849px;width:608px"></div>

<div class="garment" role="img" aria-label="Girls' scoop neck t-shirt with chest and waist measurement lines" style="left:287px;top:880px;width:110px;height:100px"></div>
<div class="size-table girls" style="left:431px;top:893px;width:477px">
  <div class="head"></div><div class="label-col" style="width:69px"></div><div class="row-line" style="left:69px"></div>
  <span class="cell h" style="left:34px">Girls</span>
  <span class="cell h" style="left:103px">XXS</span><span class="cell h" style="left:168px">XS</span><span class="cell h" style="left:237px">S</span><span class="cell h" style="left:307px">M</span><span class="cell h" style="left:377px">L</span><span class="cell h" style="left:443px">XL</span>
  <span class="cell chest" style="left:34px">Chest</span>
  <span class="cell chest" style="left:103px">19-22</span><span class="cell chest" style="left:168px">22-25</span><span class="cell chest" style="left:237px">25-28</span><span class="cell chest" style="left:307px">28-31</span><span class="cell chest" style="left:377px">31-34</span><span class="cell chest" style="left:443px">34-37</span>
  <span class="cell waist" style="left:34px">Waist</span>
  <span class="cell waist" style="left:103px">18-20</span><span class="cell waist" style="left:168px">20-22</span><span class="cell waist" style="left:237px">22-24</span><span class="cell waist" style="left:307px">24-26</span><span class="cell waist" style="left:377px">26-28</span><span class="cell waist" style="left:443px">28-30</span>
</div>

</body>
</html>
```